Commercial and Multifamily informational website

We need a website for our commercial real estate management company. We will manage offices, retail, apartments and others. Here is the brief verbiage: Providing quality commercial and multifamily portfolio management to Landlords, REITs, and financial institutions. 

Industry/Entity Type

Real Estate

Number of Pages Required

2 page

Font styles to use
Sans Serif
Other font styles liked:
• Muli, Garamond

Colors
0555a3
5c5c5c
3176b5
85acd3
474747

Requirements
Must have
• Home page and contact page

```html
<!DOCTYPE html>
<html lang="en">
<head>
<meta charset="utf-8">
<title>Kestrel Realty Management</title>
<link href="https://fonts.googleapis.com/css2?family=Mulish:wght@300;400;600;700&family=Open+Sans:wght@400;600&display=swap" rel="stylesheet">
<style>
:root{
  --brand:#2f5fa3;
  --brand-deep:#0555a3;
  --brand-mid:#3176b5;
  --brand-light:#85acd3;
  --ink:#474747;
  --ink-soft:#5c5c5c;
  --muted:#9a9a9a;
  --paper:#f6f6f7;
  --white:#ffffff;
  --dark:#2b2b2b;
  --darker:#1f1f1f;
  --field:#e4e4e4;
  --btn-grey:#6b6660;
}
*{box-sizing:border-box;margin:0;padding:0}
html,body{width:1200px;height:3267px;overflow:hidden}
body{font-family:"Mulish",sans-serif;color:var(--ink);background:var(--white);position:relative}
.wrap{position:absolute;left:0;width:1200px}

/* header */
.site-header{top:0;height:113px;background:linear-gradient(180deg,#3a69ad,#2c5a9b);}
.brand{position:absolute;left:26px;top:14px;display:flex;align-items:center;gap:12px;color:var(--white)}
.brand-mark{width:30px;height:30px;border:2px solid var(--white)}
.brand-name{font-weight:600;font-size:26px;letter-spacing:1px}
.brand-sub{font-weight:300;font-size:13px;line-height:1.1;text-transform:uppercase;margin-left:4px}
.connect{position:absolute;right:98px;top:14px;color:var(--white);display:flex;gap:10px;align-items:center}
.connect small{display:block;font-size:11px;color:#c9d8ee;text-transform:uppercase}
.connect strong{font-size:19px;font-weight:600}
.main-nav{position:absolute;top:76px;left:0;width:1200px;height:34px;background:#2a5696;border-top:1px solid #4d7bbd;display:flex;justify-content:center;align-items:center}
.main-nav a{color:var(--white);text-decoration:none;font-family:"Open Sans",sans-serif;font-size:12px;text-transform:uppercase;padding:0 12px;border-right:1px solid #6f93c6;line-height:14px}
.main-nav a:last-child{border-right:none}

/* hero */
.hero{top:113px;height:562px}
.hero-photo{position:absolute;inset:0;background:radial-gradient(ellipse at 50% 45%,#f2f3f5 0%,#dcdfe3 45%,#b9bec4 100%)}
.hero-logo{position:absolute;left:0;width:1200px;top:180px;text-align:center;font-size:70px;font-weight:700;color:var(--brand);letter-spacing:2px}
.hero-tagline{position:absolute;left:295px;top:290px;font-size:35px;font-weight:400;color:#6a6a6a}
.hero-tagline span{display:block;font-size:27px;margin-left:245px;margin-top:-6px;color:#5a5a5a}

/* search */
.search-bar{top:675px;height:77px;background:var(--brand);display:flex;align-items:center;padding-left:111px;gap:10px}
.search-bar .field{height:38px;background:var(--white);border:1px solid #d8d8d8;font-size:10px;color:#9b9b9b;padding:0 8px;display:flex;align-items:center;justify-content:space-between}
.search-btn{width:108px;height:38px;background:var(--btn-grey);color:var(--white);font-weight:700;font-size:15px;display:flex;align-items:center;justify-content:center}

/* services */
.services{top:752px;height:643px;background:var(--paper)}
.section-title{text-align:center;font-weight:300;font-size:38px;color:#555}
.services .section-title{position:absolute;top:55px;width:1200px}
.title-rule{position:absolute;top:80px;height:1px;background:#dcdcdc;width:210px}
.services-intro{position:absolute;top:118px;left:340px;width:520px;text-align:center;font-size:12px;line-height:20px;color:#aaa}
.service-card{position:absolute;top:189px;width:227px;height:392px}
.service-card .panel{position:absolute;top:110px;left:0;width:227px;height:282px;background:var(--brand);border-radius:0}
.service-card .photo{position:absolute;top:0;left:0;width:227px;height:227px;border-radius:50%;border:3px solid var(--white);background:linear-gradient(180deg,#6fa6dc 0%,#a9c9ea 45%,#c9c2b4 75%,#8a8e94 100%)}
.service-card .photo.alt{background:linear-gradient(180deg,#6aa4de 0%,#bcd7ef 35%,#e6dcc5 60%,#9d9586 100%)}
.service-card h3{position:absolute;top:240px;width:100%;text-align:center;color:var(--white);font-weight:400;font-size:21px;text-transform:uppercase}
.service-card p{position:absolute;top:275px;left:14px;width:199px;text-align:center;font-size:11px;line-height:16px;color:var(--brand-light)}
.service-card .more{position:absolute;top:346px;left:40px;width:147px;height:20px;border:1px solid #6e92c5;color:var(--white);font-size:10px;text-align:center;line-height:18px;text-transform:uppercase}

/* welcome */
.welcome{top:1400px;height:567px;background:#fbfbfc}
.welcome-photo{position:absolute;left:0;top:0}
.welcome h2{position:absolute;left:560px;width:580px;top:50px;text-align:center;font-weight:400;font-size:27px;line-height:35px;color:#555}
.divider{position:absolute;top:140px;left:560px;width:580px;height:24px}
.welcome .copy{position:absolute;left:558px;width:520px;top:190px;text-align:center;font-size:12.5px;line-height:23px;color:#555}
.welcome .copy p+p{margin-top:22px}

/* testimonials */
.testimonials{top:1967px;height:461px;background:var(--brand)}
.testimonials .section-title{position:absolute;top:50px;width:1200px;color:var(--white);font-size:30px;font-weight:400}
.quote-card{position:absolute;top:120px;width:305px;height:291px}
.quote-card .box{position:absolute;top:50px;left:0;width:305px;height:241px;background:var(--white)}
.quote-card .avatar{position:absolute;top:0;left:90px;width:124px;height:124px;border-radius:50%;border:4px solid var(--white);background:radial-gradient(circle at 50% 40%,#d7a08a 0%,#a9594a 55%,#5b3128 100%)}
.quote-card h4{position:absolute;top:134px;width:100%;text-align:center;font-family:"Open Sans",sans-serif;font-weight:600;font-size:12px;color:#333}
.quote-card p{position:absolute;top:170px;left:38px;width:229px;text-align:center;font-size:11px;line-height:16px;color:#999}
.quote-card .read{position:absolute;top:251px;left:106px;width:93px;height:24px;background:#3b4a66;color:var(--white);font-size:10px;text-align:center;line-height:24px}

/* quick form */
.quick-form{top:2428px;height:125px;background:var(--white)}
.quick-form .field{position:absolute;top:47px;height:36px;width:296px;background:var(--field);font-size:10px;color:#999;padding:12px 10px}
.quick-form .submit{position:absolute;top:47px;left:882px;width:98px;height:32px;background:#2c4a80;color:var(--white);font-size:13px;text-align:center;line-height:32px}

/* contact */
.contact{top:2553px;height:365px}
.map{position:absolute;inset:0;background:linear-gradient(135deg,#eceeef,#e2e6e4 50%,#e9ebe7)}
.contact .section-title{position:absolute;top:50px;width:1200px;font-size:30px;font-weight:400;color:#555}
.locate{position:absolute;left:145px;top:112px;font-size:13px;font-weight:600;color:#555}
.contact-line{position:absolute;left:145px;display:flex;gap:20px;font-size:10px;line-height:15px;color:#444}
.ask{position:absolute;left:612px;top:112px;font-size:13px;font-weight:600;color:#555}
.contact-form .field{position:absolute;height:26px;background:rgba(255,255,255,.7);border:1px solid #d0d0d0;font-size:10px;color:#777;padding:6px 8px}
.contact-form .send{position:absolute;left:612px;top:271px;width:130px;height:24px;background:#2c4a80;color:var(--white);font-size:11px;text-align:center;line-height:24px}

/* footer */
.site-footer{top:2918px;height:301px;background:var(--dark);color:var(--white)}
.site-footer h5{position:absolute;top:62px;font-weight:400;font-size:18px}
.quick-links{position:absolute;top:108px;left:111px;display:grid;grid-template-columns:152px 160px;row-gap:11px;font-size:11px;text-transform:uppercase;color:#ddd}
.footer-rule{position:absolute;top:80px;width:1px;height:170px;background:#444}
.tweet{position:absolute;left:506px;width:215px;font-size:11px;line-height:20px;color:#ddd;display:flex;gap:6px}
.address{position:absolute;left:853px;top:110px;font-size:11px;line-height:22px;text-transform:uppercase;color:#ddd}
.bottom-bar{top:3219px;height:48px;background:var(--darker);color:#bbb;font-size:10px}
.bottom-bar .legal{position:absolute;left:111px;top:17px;font-style:italic}
.social{position:absolute;right:111px;top:15px;display:flex;gap:6px}
.social span{width:16px;height:16px;background:#7a7a7a}
</style>
</head>
<body>

<header class="wrap site-header">
  <div class="brand">
    <span class="brand-mark"></span>
    <span class="brand-name">KRM</span>
    <span class="brand-sub">Kestrel<br>Realty<br>Management</span>
  </div>
  <div class="connect">
    <svg width="18" height="22" viewBox="0 0 18 22"><rect x="3" y="1" width="12" height="20" rx="2" fill="none" stroke="#fff" stroke-width="2"/><rect x="7" y="17" width="4" height="1.6" fill="#fff"/></svg>
    <div><small>Connect</small><strong>555 010 2477</strong></div>
  </div>
  <nav class="main-nav">
    <a>Home</a><a>About Us</a><a>Procedures</a><a>Promotions</a><a>Financing</a><a>Testimonials</a><a>Overnight Care</a><a>Patient Portal</a><a>Our Blog</a><a>Contact</a>
  </nav>
</header>

<section class="wrap hero">
  <div class="hero-photo" role="img" aria-label="Blurred photo of a bright office corridor"></div>
  <div class="hero-logo">KRM</div>
  <div class="hero-tagline">Providing quality portfolio management<span>One creative tagline at a time</span></div>
</section>

<form class="wrap search-bar">
  <div class="field" style="width:205px">Enter Your Name</div>
  <div class="field" style="width:205px">Enter E-Mail Address</div>
  <div class="field" style="width:205px">Enter Phone Number</div>
  <div class="field" style="width:205px">Select Date
    <svg width="14" height="13" viewBox="0 0 14 13"><rect x="1" y="2" width="12" height="10" fill="none" stroke="#888"/><line x1="1" y1="5" x2="13" y2="5" stroke="#888"/></svg>
  </div>
  <div class="search-btn">SEARCH</div>
</form>

<section class="wrap services">
  <div class="title-rule" style="left:235px"></div>
  <div class="title-rule" style="left:755px"></div>
  <h2 class="section-title">Our Services</h2>
  <p class="services-intro">Lorem ipsum dolor sit amet, consectetur adipiscing elit. Sed quis nisl lacinia, efficitur orci venenatis, auctor magna. Nullam auctor porttitor faucibus.</p>

  <article class="service-card" style="left:111px">
    <div class="panel"></div>
    <div class="photo" role="img" aria-label="Photo of a glass office tower"></div>
    <h3>Offices</h3>
    <p>Lorem ipsum dolor sit amet, consectetur adipiscing elit. Sed quis nisl lacinia efficitur orci.</p>
    <div class="more">More</div>
  </article>
  <article class="service-card" style="left:362px">
    <div class="panel"></div>
    <div class="photo alt" role="img" aria-label="Photo of an apartment building"></div>
    <h3>Appartaments</h3>
    <p>Lorem ipsum dolor sit amet, consectetur adipiscing elit. Sed quis nisl lacinia efficitur orci.</p>
    <div class="more">More</div>
  </article>
  <article class="service-card" style="left:614px">
    <div class="panel"></div>
    <div class="photo alt" role="img" aria-label="Photo of a retail building"></div>
    <h3>Retail</h3>
    <p>Lorem ipsum dolor sit amet, consectetur adipiscing elit. Sed quis nisl lacinia efficitur orci.</p>
    <div class="more">More</div>
  </article>
  <article class="service-card" style="left:865px">
    <div class="panel"></div>
    <div class="photo" role="img" aria-label="Photo of a housing tower"></div>
    <h3>Housing</h3>
    <p>Lorem ipsum dolor sit amet, consectetur adipiscing elit. Sed quis nisl lacinia efficitur orci.</p>
    <div class="more">More</div>
  </article>
</section>

<section class="wrap welcome">
  <svg class="welcome-photo" width="540" height="567" viewBox="0 0 540 567" role="img" aria-label="Photo of a suburban house at dusk">
    <defs>
      <linearGradient id="dusk" x1="0" y1="0" x2="0" y2="1">
        <stop offset="0" stop-color="#8b95c4"/>
        <stop offset=".45" stop-color="#c9a6b6"/>
        <stop offset=".7" stop-color="#4b5466"/>
        <stop offset="1" stop-color="#3b3f48"/>
      </linearGradient>
    </defs>
    <path d="M0 0 H330 C470 90 540 210 520 330 C505 430 450 520 380 567 H0 Z" fill="url(#dusk)"/>
    <path d="M330 0 C470 90 540 210 520 330 C505 430 450 520 380 567" fill="none" stroke="#2f5fa3" stroke-width="3"/>
  </svg>
  <h2>Welcome to Kestrel Realty Management,<br>located in sunny Fairhaven, CA.</h2>
  <svg class="divider" viewBox="0 0 580 24">
    <line x1="30" y1="12" x2="265" y2="12" stroke="#bbb"/>
    <line x1="315" y1="12" x2="550" y2="12" stroke="#bbb"/>
    <circle cx="290" cy="12" r="11" fill="#e6e9ee"/>
    <circle cx="290" cy="12" r="4" fill="#2f5fa3"/>
  </svg>
  <div class="copy">
    <p>Lorem ipsum dolor sit amet, consectetur adipiscing elit. Vivamus feugiat dapibus blandit libero ut condimentum. Fusce eget sodales dolor. Aenean vel ante nibh. Morbi sed elit ut libero malesuada malesuada. Vivamus rhoncus ante sem consequat laoreet. Donec imperdiet venenatis feugiat. Aenean faucibus sem vel augue, id ultricies tellus sagittis vel. In ornare accumsan lorem in vestibulum, dapibus tempus.</p>
    <p>Quisque lorem commodo. Sed rutrum sagittis neque quis vulputate. Sed quam nisi non aliquet a, pellentesque nec eros. Proin vitae laoreet magna, eget sem. Lorem ipsum dolor sit amet, consectetur adipiscing elit. Vivamus feugiat. Curabitur porttitor nec risus sit amet faucibus. Morbi non neque varius, bibendum placerat nulla. Morbi ut aliquam nulla. Donec luctus ultrices arcu. Lorem.</p>
  </div>
</section>

<section class="wrap testimonials">
  <h2 class="section-title">Testimonials</h2>
  <article class="quote-card" style="left:111px">
    <div class="box"></div>
    <div class="avatar" role="img" aria-label="Portrait of a client"></div>
    <h4>adipiscing elit. Vestibulum non euismod</h4>
    <p>Lorem ipsum dolor sit amet, consectetur adipiscing elit. Vestibulum non euismod est. Aliquam dignissim velit mi, eget sollicitudin.</p>
    <div class="read">Read More</div>
  </article>
  <article class="quote-card" style="left:449px">
    <div class="box"></div>
    <div class="avatar" role="img" aria-label="Portrait of a client"></div>
    <h4>adipiscing elit. Vestibulum non euismod</h4>
    <p>Lorem ipsum dolor sit amet, consectetur adipiscing elit. Vestibulum non euismod est. Aliquam dignissim velit mi, eget sollicitudin.</p>
    <div class="read">Read More</div>
  </article>
  <article class="quote-card" style="left:782px">
    <div class="box"></div>
    <div class="avatar" role="img" aria-label="Portrait of a client"></div>
    <h4>adipiscing elit. Vestibulum non euismod</h4>
    <p>Lorem ipsum dolor sit amet, consectetur adipiscing elit. Vestibulum non euismod est. Aliquam dignissim velit mi, eget sollicitudin.</p>
    <div class="read">Read More</div>
  </article>
</section>

<form class="wrap quick-form">
  <div class="field" style="left:218px">Name</div>
  <div class="field" style="left:554px">Phone no</div>
  <div class="submit">SUBMIT</div>
</form>

<section class="wrap contact">
  <div class="map" role="img" aria-label="Faded street map of the office neighbourhood"></div>
  <h2 class="section-title">CONTACT US</h2>
  <div class="locate">We are conveniently located at:</div>
  <div class="contact-line" style="top:148px">
    <svg width="12" height="16" viewBox="0 0 12 16"><path d="M6 0C2.7 0 0 2.6 0 5.8 0 10 6 16 6 16s6-6 6-10.2C12 2.6 9.3 0 6 0z" fill="#333"/><circle cx="6" cy="5.8" r="2.2" fill="#eee"/></svg>
    <span>2280 ALDER GROVE AVE, SUITE C<br>FAIRHAVEN, CA 90410</span>
  </div>
  <div class="contact-line" style="top:194px">
    <svg width="12" height="14" viewBox="0 0 12 14"><path d="M2 0l3 3-1.5 2c.8 1.8 2.2 3.3 4 4.2L9.5 8 12 11l-2 3C5 13 1 9 0 2z" fill="#333"/></svg>
    <span>555.014.3862<br>555.014.0061</span>
  </div>
  <div class="ask">Questions about options? Contact us.</div>
  <div class="contact-form">
    <div class="field" style="left:612px;top:148px;width:208px">Name</div>
    <div class="field" style="left:846px;top:148px;width:208px">Email</div>
    <div class="field" style="left:612px;top:186px;width:442px;height:68px">Message</div>
    <div class="send">Send</div>
  </div>
</section>

<footer class="wrap site-footer">
  <h5 style="left:111px">Quick Link</h5>
  <div class="quick-links">
    <span>Home</span><span>Testimonials</span>
    <span>About Us</span><span>Overnight Care</span>
    <span>Procedures</span><span>Patient Portal</span>
    <span>Promotions</span><span>Our Blog</span>
    <span>Financing</span><span>Contact</span>
  </div>
  <div class="footer-rule" style="left:433px"></div>
  <h5 style="left:524px">Contact Details</h5>
  <div class="tweet" style="top:104px">
    <svg width="14" height="12" viewBox="0 0 14 12"><path d="M0 6l14-6-3 12-4-3-2 3V8l6-6-8 5z" fill="#999"/></svg>
    <span>Lorem ipsum dolor sit amet, consectetur adipiscing elit. Nam suscipit, ligula et est.</span>
  </div>
  <div class="tweet" style="top:182px">
    <svg width="14" height="12" viewBox="0 0 14 12"><path d="M0 6l14-6-3 12-4-3-2 3V8l6-6-8 5z" fill="#999"/></svg>
    <span>Lorem ipsum dolor sit amet, consectetur adipiscing elit. Nam suscipit, ligula et est.</span>
  </div>
  <div class="footer-rule" style="left:767px"></div>
  <h5 style="left:853px">Contact Details</h5>
  <div class="address">We are conveniently located at:<br>2280 Alder Grove Ave, Suite C<br>Fairhaven, CA 90410<br>P / 555.014.3862<br>F / 555.014.0061</div>
</footer>

<div class="wrap bottom-bar">
  <span class="legal">Kestrel Realty. All Rights Reserved</span>
  <div class="social"><span></span><span></span><span></span><span></span></div>
</div>

</body>
</html>
```